BRISLEY Homes business card Coral Press

I've been a Real Estate agent since 1988. I left the BIG brokerages 2 years ago and am on my own and need a business card. I love doing graphics, but don't have the bandwidth right now.

Background. I want a card that stands out like I do. I'm the fun guy that always has a joke or funny story, and my clients like me. Something fun, but not too silly.

I don't have a symbol or logo that I'm using on the card now, but need to include something, a Font by itself or a logo? I'm not sure if we need a logo or not. I'm open.
The GREAT design is going to be the basis for the next project of stationary, note pads, and Real Estate FOR SALE & Open House signs.

Single sided card is fine, but I selected a 2 sided just in case that's what it works out to be.

Here we go. If you need anything else. Please let me know. As I think of anything, I'll add that also.

Target Market(s)

My territory is Santa Clara County / Silicon Valley, CA. I tend to work with new buyers buying a condo ($500,000) up to single family home for about $1.5 million. 1st time buyers and also move-up buyers. I haven't worked with multi-million $$ homes .... but wouldn't turn it down. Clients here tend to be White, Latin and now many more Chinese and East Indians. Clients also tend to be high tech, Zentrix, Quill, Mingleverse workers and also non tech people.

Industry/Entity Type

Business

Contact Information for Business Card

CONTENT:
Company: BRISLEY Homes
My name: Harold P. Brisley Jr.
Title: Real Estate Broker
Email: Hal@HaroldBrisley.example
Website: www.HaroldBrisley.example
Phone: (408) 555-0172
BRE # 07390418

Font styles to use
Sans Serif

Requirements
Must have
• Content from above. Something that stands out from the others. Serious enough looking, not stale, maybe a bit fun.

```html
<!DOCTYPE html>
<html lang="en">
<head>
<meta charset="utf-8">
<title>BRISLEY Homes business card</title>
<link rel="stylesheet" href="https://fonts.googleapis.com/css2?family=Josefin+Sans:wght@400;600&display=swap">
<style>
  :root {
    --stage: #e9e7e3;
    --card-orange: #e04e1f;
    --paper-white: #f3f1ee;
    --ink-black: #1c1b1b;
    --label-black: #1e1d1d;
    --tile-light: #ebebeb;
    --tile-dark: #111111;
  }
  * { box-sizing: border-box; margin: 0; padding: 0; }
  html, body {
    width: 1200px;
    height: 1000px;
    overflow: hidden;
    background: var(--stage);
    font-family: "Josefin Sans", sans-serif;
  }
  .canvas {
    position: relative;
    width: 1200px;
    height: 1000px;
  }

  /* Portrait business card, flat */
  .business-card {
    position: absolute;
    left: 90px;
    top: 60px;
    width: 520px;
    height: 880px;
    background: var(--card-orange);
    box-shadow: 0 10px 30px rgba(0, 0, 0, 0.18);
    overflow: hidden;
  }
  .contact-strip {
    position: absolute;
    left: 0;
    top: 0;
    width: 100%;
    height: 170px;
    background: var(--paper-white);
    padding: 34px 36px 0 0;
    text-align: right;
    font-size: 24px;
    font-weight: 400;
    line-height: 1.4;
    letter-spacing: 0.5px;
    color: var(--ink-black);
  }
  .contact-strip .website { color: var(--card-orange); }

  .name-label {
    position: absolute;
    left: 0;
    top: 220px;
    width: 340px;
    padding: 22px 20px 18px 34px;
    background: var(--label-black);
    color: var(--paper-white);
  }
  .name-label .person-name {
    font-size: 26px;
    font-weight: 600;
    letter-spacing: 0.5px;
  }
  .name-label .person-title {
    margin-top: 6px;
    font-size: 22px;
    font-weight: 400;
  }

  /* Company name, set in the card's text font, reading upward */
  .company-name {
    position: absolute;
    left: 60px;
    top: 510px;
    width: 480px;
    height: 220px;
    transform: rotate(-90deg);
    transform-origin: center;
    color: var(--paper-white);
    font-size: 100px;
    font-weight: 400;
    line-height: 1.05;
    text-align: left;
  }
  .company-name span { display: block; white-space: nowrap; }

  /* Name on dark and light grounds */
  .name-tile {
    position: absolute;
    left: 680px;
    width: 430px;
    height: 150px;
    display: flex;
    align-items: center;
    justify-content: center;
    font-size: 42px;
    font-weight: 400;
    letter-spacing: 0.5px;
  }
  .name-tile--dark {
    top: 610px;
    background: var(--tile-dark);
    color: var(--paper-white);
  }
  .name-tile--light {
    top: 790px;
    background: var(--tile-light);
    color: var(--ink-black);
  }
</style>
</head>
<body>
<main class="canvas">
  <section class="business-card" aria-label="BRISLEY Homes business card">
    <div class="contact-strip">
      <p class="website">www.HaroldBrisley.example</p>
      <p class="email">e. Hal@HaroldBrisley.example</p>
      <p class="phone">t. (408) 555-0172</p>
    </div>

    <div class="name-label">
      <p class="person-name">Harold P. Brisley Jr.</p>
      <p class="person-title">Real Estate Broker</p>
    </div>

    <h1 class="company-name">
      <span>BRISLEY</span>
      <span>Homes</span>
    </h1>
  </section>

  <p class="name-tile name-tile--dark">BRISLEY Homes</p>
  <p class="name-tile name-tile--light">BRISLEY Homes</p>
</main>
</body>
</html>
```